Consulting and investment firm, logo design is needed as well.

I am looking to open a consulting firm. Where myself is currently an investor, entrepreneur and consultant for many businesses.

The company name is Torvique Company Limited
The logo should communicate prestige like luxury or gold or money, trustworthy and modern.

Overall name card Color can be: white, black, blue, gold, silver (you can choose one, few or all of it, up to you)

It would be great if you can provide raw file like .psd for me so that I can make some little amendment in future and inserting company name or remove it. Because I would also like to use it as only under my name too (some card I will remove the company name).

• I want it to look modern.

```html
<!DOCTYPE html>
<html lang="en">
<head>
<meta charset="UTF-8">
<title>Torvique Company Limited — Business Card</title>
<link rel="stylesheet" href="https://fonts.googleapis.com/css2?family=Montserrat:wght@400;500;600;700&display=swap">
<style>
  :root {
    --backdrop: #d9d8d4;
    --card-black: #1b1b1b;
    --gold: #c99a3a;
    --gold-light: #e2bb5c;
    --white: #f4f4f2;
  }
  * { box-sizing: border-box; margin: 0; padding: 0; }
  html, body { width: 1200px; height: 938px; overflow: hidden; }
  body {
    background: var(--backdrop);
    font-family: "Montserrat", Arial, sans-serif;
    display: flex;
    align-items: center;
    justify-content: center;
    gap: 40px;
  }
  .card {
    width: 540px;
    height: 309px;
    background: var(--card-black);
    border: 2px solid var(--gold);
    border-radius: 3px;
    box-shadow: 0 10px 28px rgba(0,0,0,0.25);
    position: relative;
    overflow: hidden;
  }

  /* brand name block */
  .brand {
    display: flex;
    flex-direction: column;
    align-items: center;
    color: var(--gold);
    font-weight: 600;
    text-transform: uppercase;
  }
  .brand-square {
    border: 3px solid var(--gold);
    margin-bottom: 14px;
  }
  .brand-name { letter-spacing: 0.12em; line-height: 1; }
  .brand-sub { letter-spacing: 0.18em; line-height: 1; margin-top: 8px; }

  /* contact side */
  .card-contact { display: flex; }
  .card-contact .brand {
    width: 232px;
    justify-content: center;
    padding-top: 6px;
  }
  .card-contact .brand-square { width: 62px; height: 62px; }
  .card-contact .brand-name { font-size: 27px; }
  .card-contact .brand-sub { font-size: 11px; }
  .divider {
    width: 1px;
    background: var(--gold);
    margin: 30px 0 54px;
  }
  .contact {
    padding: 34px 0 0 26px;
    color: var(--white);
    font-size: 13.5px;
    line-height: 1.45;
  }
  .person-name {
    color: var(--gold-light);
    font-weight: 700;
    font-size: 17px;
    letter-spacing: 0.04em;
    text-transform: uppercase;
  }
  .person-role { margin-bottom: 10px; }
  .address { margin-bottom: 10px; }
  .contact-line { display: flex; align-items: center; gap: 8px; }
  .contact-line svg { width: 12px; height: 12px; fill: var(--gold); flex: none; }
  .highlight { color: var(--gold-light); }

  /* logo side */
  .card-logo {
    display: flex;
    align-items: center;
    justify-content: center;
  }
  .card-logo .brand-square { width: 80px; height: 80px; margin-bottom: 20px; }
  .card-logo .brand-name { font-size: 44px; }
  .card-logo .brand-sub { font-size: 17px; margin-top: 12px; }
</style>
</head>
<body>

  <section class="card card-contact" aria-label="Card back with contact details">
    <div class="brand">
      <div class="brand-square"></div>
      <span class="brand-name">Torvique</span>
      <span class="brand-sub">Company Limited</span>
    </div>
    <div class="divider"></div>
    <div class="contact">
      <p class="person-name">Marcus Delane</p>
      <p class="person-role">Sales Representative</p>
      <p class="address">48 Elm Ridge Road<br>Westbrook, CT 06498</p>
      <p class="contact-line">
        <svg viewBox="0 0 24 24" aria-hidden="true"><path d="M6.6 10.8a15.1 15.1 0 0 0 6.6 6.6l2.2-2.2a1 1 0 0 1 1-.25 11.4 11.4 0 0 0 3.6.57 1 1 0 0 1 1 1V20a1 1 0 0 1-1 1A17 17 0 0 1 3 4a1 1 0 0 1 1-1h3.5a1 1 0 0 1 1 1c0 1.25.2 2.45.57 3.57a1 1 0 0 1-.25 1z"/></svg>
        860-555-0147
      </p>
      <p class="contact-line">
        <svg viewBox="0 0 24 24" aria-hidden="true"><path d="M2 5h20v14H2z M4 7v.4l8 5 8-5V7z" fill-rule="evenodd"/></svg>
        info@torvique.com.au
      </p>
      <p class="contact-line">
        <svg viewBox="0 0 24 24" aria-hidden="true"><circle cx="12" cy="12" r="10"/></svg>
        <span>www.<span class="highlight">torvique</span>.com.au</span>
      </p>
    </div>
  </section>

  <section class="card card-logo" aria-label="Card front">
    <div class="brand">
      <div class="brand-square"></div>
      <span class="brand-name">Torvique</span>
      <span class="brand-sub">Company Limited</span>
    </div>
  </section>

</body>
</html>
```